URGENT Conference Banner ad to attract a crowd!

I need please in my brand colours 2 x static ads with this copy please:
Have an online business?
Make your customers stick!
It really needs to stand out but not be offensive.
I would like to see blue background on white font and then the reverse. on the white one, it needs a thin blue border around it.
I need it in static: 300x250 and 300x600.
on this one - 300x600. please add a circle saying register now!
Please see examples of other messages I have done. I need this URGENTLY pelase :)
Target Market(s)
http://www.tradefairvantora.com.au/en/home/
Industry/Entity Type
Business
Font styles to use
Other font styles liked:
- roboto font
Requirements
Must have
- Use this blue:
- 00b6ce
- roboto font
Nice to have
- look and feel like my banners supplied

```html
<!DOCTYPE html>
<html lang="en">
<head>
<meta charset="utf-8">
<title>Tradefair Vantora – Banner Ads</title>
<link rel="stylesheet" href="https://fonts.googleapis.com/css2?family=Roboto:wght@300;400;700;900&display=swap">
<style>
  :root {
    --brand-blue: #00b6ce;
    --badge-blue: #1a93d6;
    --badge-deep: #0b6fb0;
    --white: #ffffff;
    --stage: #d6ae88;
    --treat-red: #b8192b;
    --treat-brown: #6b3a1c;
    --treat-amber: #c77a2e;
  }
  * { box-sizing: border-box; margin: 0; padding: 0; }
  html, body { width: 1200px; height: 900px; overflow: hidden; }
  body {
    background: var(--stage);
    font-family: "Roboto", Arial, sans-serif;
    position: relative;
  }
  .banner {
    position: absolute;
    background: var(--white);
    border: 7px solid var(--brand-blue);
    color: var(--brand-blue);
    text-align: center;
    overflow: hidden;
  }
  .banner--rectangle { left: 270px; top: 332px; width: 349px; height: 291px; }
  .banner--skyscraper { left: 679px; top: 127px; width: 351px; height: 703px; }

  .brand { position: absolute; left: 0; right: 0; font-weight: 300; line-height: 1; color: var(--brand-blue); }
  .brand__name { display: block; text-align: center; }
  .brand__tag { display: block; text-align: right; }

  .banner--rectangle .brand { top: 2px; padding-right: 18px; }
  .banner--rectangle .brand__name { font-size: 50px; letter-spacing: 0.5px; }
  .banner--rectangle .brand__tag { font-size: 22px; }

  .banner--skyscraper .brand { top: 14px; padding-right: 18px; }
  .banner--skyscraper .brand__name { font-size: 54px; letter-spacing: 0.5px; }
  .banner--skyscraper .brand__tag { font-size: 22px; margin-top: 2px; }

  .headline { position: absolute; left: 0; right: 0; font-weight: 700; }
  .banner--rectangle .headline { top: 86px; font-size: 22px; line-height: 28px; }
  .banner--skyscraper .headline--question { top: 118px; font-size: 37px; line-height: 64px; }
  .banner--skyscraper .headline--hook { top: 426px; font-size: 32px; line-height: 50px; }

  .product-photo {
    position: absolute;
    left: 50%;
    transform: translateX(-50%);
    border-radius: 24px;
    background:
      radial-gradient(ellipse at 50% 60%, rgba(184, 25, 43, 0.85) 0%, rgba(107, 58, 28, 0.55) 45%, rgba(199, 122, 46, 0.15) 75%, rgba(255, 255, 255, 0) 100%);
  }
  .banner--rectangle .product-photo { top: 150px; width: 160px; height: 118px; }
  .banner--skyscraper .product-photo { top: 240px; width: 200px; height: 182px; }

  .register-badge {
    position: absolute;
    left: 50%;
    top: 540px;
    width: 140px;
    height: 140px;
    transform: translateX(-50%);
  }
</style>
</head>
<body>

  <section class="banner banner--rectangle" aria-label="Tradefair Vantora 300 by 250 banner">
    <div class="brand">
      <span class="brand__name">tradefair</span>
      <span class="brand__tag">vantora &amp; Expo</span>
    </div>
    <h1 class="headline">HAVE AN ONLINE BUSINESS?<br>Make your customers stick!</h1>
    <div class="product-photo" role="img" aria-label="Photo of assorted toffee and chocolate candy apples on sticks"></div>
  </section>

  <section class="banner banner--skyscraper" aria-label="Tradefair Vantora 300 by 600 banner">
    <div class="brand">
      <span class="brand__name">tradefair</span>
      <span class="brand__tag">vantora &amp; Expo</span>
    </div>
    <h1 class="headline headline--question">HAVE AN ONLINE<br>BUSINESS?</h1>
    <div class="product-photo" role="img" aria-label="Photo of assorted toffee and chocolate candy apples on sticks"></div>
    <p class="headline headline--hook">Make your customers<br>stick!</p>
    <svg class="register-badge" viewBox="0 0 140 140" role="img" aria-label="Register now">
      <defs>
        <radialGradient id="badge-fill" cx="40%" cy="35%" r="70%">
          <stop offset="0" stop-color="#1a93d6"/>
          <stop offset="1" stop-color="#0b6fb0"/>
        </radialGradient>
      </defs>
      <circle cx="70" cy="72" r="64" fill="#000" opacity="0.18"/>
      <circle cx="68" cy="68" r="64" fill="url(#badge-fill)"/>
      <circle cx="68" cy="68" r="57" fill="none" stroke="#ffffff" stroke-width="1.5" stroke-dasharray="2 3"/>
      <g transform="rotate(8 68 68)" fill="#ffffff" font-family="Roboto, Arial, sans-serif" font-weight="700" text-anchor="middle">
        <text x="68" y="60" font-size="20">REGISTER</text>
        <text x="68" y="92" font-size="32" font-weight="900">NOW!</text>
      </g>
    </svg>
  </section>

</body>
</html>
```